Wanting a leaflet that can be letter boxed to surronding areas to my workshop.

Will need it to display -
Tarrow Automotive Location

Contact details- (maybe even a little street map?)
4/2-5 Pellick Lane,
Bayswater North
9358 2149
info@tarrowautomotive.example.au
www.tarrowautomotive.example.au

Services include -
Log book servicing
Mechanical repairs
Pre sale inspections
Great Service and Advice
Weeekend Servicing (This needs to be a big point to get across)

Service Special - $179*
Includes
Engine Oil and filter replacement using factory approved parts
Wheel rotation
Brake inspection
Cooling system test
Saftey inspection

*Large cars $249

Target Market(s)

People in areas close to workshop location, uni students, performance cars, parents

Industry/Entity Type

Automotive

Requirements
Must have
• Tarrow Automotive logo

```html
<!DOCTYPE html>
<html lang="en">
<head>
<meta charset="utf-8">
<title>Tarrow Automotive – Service Special Leaflet</title>
<link rel="stylesheet" href="https://fonts.googleapis.com/css2?family=Source+Sans+3:ital,wght@0,400;0,600;0,700;1,700&display=swap">
<style>
  :root {
    --paper: #ffffff;
    --frame-line: #1a1a1a;
    --brand-red: #c8161d;
    --brand-navy: #1c1f6b;
    --text-dark: #111111;
    --large-blue: #1f4f8a;
    --map-frame: #a9a9a9;
    --map-fill: #e6e3dc;
    --footer-black: #050505;
    --footer-grey: #6e6e6e;
    --photo-warm: #d98a2b;
    --photo-sky: #f2efe6;
    --photo-road: #3b3a3a;
  }
  * { margin: 0; padding: 0; box-sizing: border-box; }
  html, body {
    width: 812px; height: 1200px; overflow: hidden;
    background: var(--paper);
    font-family: "Source Sans 3", "Myriad Pro", Arial, sans-serif;
    color: var(--text-dark);
  }
  .leaflet { position: relative; width: 812px; height: 1200px; background: var(--paper); }
  .frame {
    position: absolute; left: 11px; top: 62px; width: 788px; height: 1125px;
    border: 1px solid var(--frame-line);
    background: linear-gradient(180deg, #ffffff 55%, #e9e9e9 80%, #ffffff 100%);
    overflow: hidden;
  }
  .brand { position: absolute; right: 28px; top: 58px; text-align: right; }
  .brand-name {
    font-weight: 700; font-size: 34px; color: var(--brand-red);
    letter-spacing: 0.5px; line-height: 1;
  }
  .brand-web { margin-top: 6px; font-size: 14px; color: #333; letter-spacing: 0.6px; }
  .top-bar {
    position: absolute; left: 0; top: 155px; width: 100%; height: 17px;
    background: linear-gradient(90deg, #ffffff 0%, #9a9a9a 45%, #000000 100%);
  }
  .hero-photo {
    position: absolute; left: 0; top: 172px; width: 100%; height: 376px;
    background:
      linear-gradient(180deg, transparent 60%, var(--photo-road) 100%),
      linear-gradient(100deg, #7a4a1c 0%, var(--photo-warm) 30%, var(--photo-sky) 60%, #c9a46a 85%, #8a5a25 100%);
  }
  .services-tab {
    position: absolute; left: 0; top: 565px; width: 272px; height: 36px;
    background: linear-gradient(90deg, var(--brand-red), #9e0f14);
    color: #fff; font-weight: 700; font-size: 22px; line-height: 36px;
    padding-left: 36px; box-shadow: 3px 4px 6px rgba(0,0,0,0.35);
  }
  .list { position: absolute; left: 44px; list-style: none; font-size: 20px; line-height: 25px; }
  .list-services { top: 611px; }
  .list-special { top: 787px; }
  .weekend-badge {
    position: absolute; left: 28px; top: 715px; width: 372px; height: 63px;
    border-radius: 10px;
    background: linear-gradient(180deg, #2b2f86, var(--brand-navy));
    color: #fff; font-weight: 700; font-size: 30px; text-align: center; line-height: 63px;
    box-shadow: 3px 5px 8px rgba(0,0,0,0.3);
  }
  .large-cars {
    position: absolute; left: 44px; top: 936px; line-height: 50px;
    font-weight: 700; font-style: italic; font-size: 42px; color: var(--large-blue);
    text-shadow: 2px 3px 4px rgba(0,0,0,0.25);
  }
  .special-oval, .special-text {
    position: absolute; left: 372px; top: 483px; width: 332px; height: 198px;
  }
  .special-text { text-align: center; color: #fff; }
  .special-price {
    font-weight: 700; font-size: 74px; line-height: 1; margin-top: 34px;
    text-shadow: 2px 3px 4px rgba(0,0,0,0.4);
  }
  .special-label {
    font-weight: 700; font-size: 27px; margin-top: 14px;
    text-shadow: 1px 2px 3px rgba(0,0,0,0.4);
  }
  .location-map {
    position: absolute; left: 468px; top: 697px; width: 301px; height: 293px;
    border: 12px solid var(--map-frame); border-radius: 16px;
    background: var(--map-fill);
  }
  .blue-line {
    position: absolute; left: 0; top: 1006px; width: 100%; height: 18px;
    background: linear-gradient(90deg, #1b2a5c 0%, #3a8fc8 50%, #1b2a5c 100%);
  }
  .footer {
    position: absolute; left: 0; top: 1024px; width: 100%; height: 101px;
    background: linear-gradient(90deg, var(--footer-grey) 0%, #2a2a2a 30%, var(--footer-black) 60%);
    color: #fff;
  }
  .contact-heading {
    position: absolute; left: 265px; top: 4px;
    font-weight: 700; font-style: italic; font-size: 19px;
  }
  .contact-lines {
    position: absolute; left: 252px; top: 34px;
    font-size: 12px; line-height: 15px; font-style: normal;
  }
  .footer-web { position: absolute; left: 570px; top: 78px; font-size: 12px; }
</style>
</head>
<body>
<div class="leaflet">
  <div class="frame">
    <div class="brand">
      <div class="brand-name">Tarrow Automotive</div>
      <div class="brand-web">www.tarrowautomotive.example.au</div>
    </div>

    <div class="top-bar"></div>
    <div class="hero-photo" role="img" aria-label="Silver sedan driving on a country road at sunset, motion blurred"></div>

    <div class="services-tab">Services include -</div>
    <ul class="list list-services">
      <li>Log book servicing</li>
      <li>Mechanical repairs</li>
      <li>Pre sale inspections</li>
      <li>Great Service and Advice</li>
    </ul>

    <svg class="special-oval" viewBox="0 0 332 198" aria-hidden="true">
      <defs>
        <radialGradient id="ovalFill" cx="50%" cy="35%" r="65%">
          <stop offset="0%" stop-color="#4f8fc4"/>
          <stop offset="60%" stop-color="#2a6aa3"/>
          <stop offset="100%" stop-color="#123f6e"/>
        </radialGradient>
      </defs>
      <ellipse cx="166" cy="99" rx="162" ry="95" fill="url(#ovalFill)" stroke="#8fb6d8" stroke-width="3"/>
    </svg>
    <div class="special-text">
      <div class="special-price">$179*</div>
      <div class="special-label">Service Special</div>
    </div>

    <div class="weekend-badge">Weeekend Servicing</div>
    <ul class="list list-special">
      <li>Engine Oil and filter replacement using</li>
      <li>factory approved parts</li>
      <li>Wheel rotation</li>
      <li>Brake inspection</li>
      <li>Cooling system test</li>
      <li>Saftey inspection</li>
    </ul>
    <div class="large-cars">Large cars $249</div>

    <div class="location-map" role="img" aria-label="Street map showing the workshop location in Bayswater North"></div>

    <div class="blue-line"></div>
    <footer class="footer">
      <div class="contact-heading">Contact details-</div>
      <address class="contact-lines">
        4/2-5 Pellick Lane,<br>
        Bayswater North<br>
        9358 2149<br>
        info@tarrowautomotive.example.au
      </address>
      <div class="footer-web">www.tarrowautomotive.example.au</div>
    </footer>
  </div>
</div>
</body>
</html>
```